Brook Forge - Crypto Currency Miner Powered by Renewable Energy Website

We Need Web Pages Design for Website for Crypto Currency Miner

Serivices include:
Mining Rig Sales
Housing for Rigs turnkey on renewable energy grid
Cloud Mining term packages
Updates

http://www.vaultrigdigest.example (Competitors sites)

Target Market(s)

Investers for Mining Rigs and terms for 1,2 or 3 years of Hash rate

Industry/Entity Type

Mining

Number of Pages Required

5+ page

Font styles to use
Sans Serif

Colors
add136
9bcb3c
606060
474747
ffc214
cadf82
fbee3e
876aae
6b449b

Requirements
Must have
• Pictures of Solar, Wind and power Factor Correction units
Nice to have
• e-commerce platform so contract terms can be purchased through website
Should not have
• Heavy construction equipment

```html
<!DOCTYPE html>
<html lang="en">
<head>
<meta charset="utf-8">
<title>Brook Forge – Crypto Currency Miner</title>
<link href="https://fonts.googleapis.com/css2?family=Mulish:wght@400;600;700&family=Open+Sans:wght@400;600&display=swap" rel="stylesheet">
<style>
:root{
  --green:#6fb52c;
  --green-light:#9bcb3c;
  --green-pale:#add136;
  --text:#474747;
  --text-soft:#606060;
  --red:#d0101b;
  --orange:#f7a81b;
  --yellow:#ffc214;
  --yellow-light:#fbd23a;
  --white:#ffffff;
  --line:#d6d6d6;
  --dark:#1d2226;
}
*{box-sizing:border-box;margin:0;padding:0}
html,body{width:1200px;height:3352px;overflow:hidden}
body{font-family:"Open Sans",Arial,sans-serif;color:var(--text);background:var(--white);position:relative}
h1,h2,h3,h4{font-family:"Mulish",Arial,sans-serif;font-weight:400}
a{color:inherit;text-decoration:none}
.section{position:absolute;left:0;width:1200px}

/* header */
.site-header{top:0;height:100px;display:flex;align-items:center;justify-content:space-between;padding:0 130px 0 120px;background:var(--white);box-shadow:0 1px 4px rgba(0,0,0,.08);z-index:2}
.brand{display:flex;align-items:center;gap:12px}
.brand-mark{width:52px;height:52px;border-radius:50%;background:var(--green)}
.brand-name{font-family:"Mulish",Arial,sans-serif;font-weight:700;font-size:32px;color:var(--text)}
.main-nav{display:flex;gap:34px;font-family:"Mulish",Arial,sans-serif;font-size:17px;color:var(--text)}
.main-nav .active{color:var(--green)}

/* hero */
.hero{top:100px;height:557px;background:linear-gradient(180deg,#9ea7ad 0%,#c9cfd0 30%,#7e9a64 55%,#5e8440 70%,#4d5a78 82%,#2f3c5c 100%);text-align:center;color:var(--white)}
.hero-title{font-family:"Mulish",Arial,sans-serif;font-weight:600;font-size:50px;letter-spacing:1px;margin-top:173px;text-shadow:0 1px 4px rgba(0,0,0,.35)}
.hero-sub{font-size:21px;line-height:31px;width:640px;margin:8px auto 0;text-shadow:0 1px 3px rgba(0,0,0,.35)}
.btn{display:inline-block;font-family:"Mulish",Arial,sans-serif;font-size:15px;text-align:center}
.btn-outline{border:2px solid var(--white);color:var(--white);width:170px;height:42px;line-height:38px}
.hero .btn{margin-top:32px}
.slider-dots{position:absolute;bottom:25px;left:0;width:100%;display:flex;justify-content:center;gap:8px}
.slider-dots span{width:11px;height:11px;border-radius:50%;background:var(--white)}
.slider-dots span.off{background:transparent;border:2px solid var(--white)}

/* intro */
.intro{top:657px;height:449px;text-align:center}
.intro-title{font-size:40px;color:var(--text);margin-top:60px}
.divider{display:flex;align-items:center;justify-content:center;gap:10px;margin-top:16px}
.divider i{width:120px;height:1px;background:#9a9a9a}
.divider b{width:36px;height:36px;border-radius:50%;background:var(--green)}
.intro-text{position:relative;z-index:1;width:760px;margin:12px auto 0;font-size:14px;line-height:29px;color:var(--text-soft)}
.network-art{position:absolute;z-index:0;left:210px;top:236px;width:780px;height:213px;background:radial-gradient(ellipse at 50% 100%,#e9e9e9 0%,#f6f6f6 50%,#ffffff 75%)}
.btn-red{background:var(--red);color:var(--white);width:136px;height:40px;line-height:40px;position:absolute;left:536px;top:276px;z-index:1}

/* services */
.services{top:1106px;height:456px;background:linear-gradient(90deg,var(--green-light),var(--green));text-align:center;color:var(--white)}
.services-title{font-size:31px;margin-top:40px}
.service-list{display:flex;justify-content:center;gap:0;margin-top:30px}
.service{width:340px;display:flex;flex-direction:column;align-items:center}
.service-icon{width:126px;height:126px;border-radius:50%;background:#111;border:5px solid #9ccc3c;box-shadow:0 0 0 3px #111;display:flex;align-items:center;justify-content:center}
.service h3{font-size:20px;line-height:23px;margin-top:22px;height:48px;display:flex;align-items:flex-end}
.service p{font-size:11px;line-height:18px;width:230px;margin-top:10px;opacity:.9}
.service .btn-outline{width:128px;height:38px;line-height:34px;margin-top:18px;font-size:14px}

/* how it works */
.how{top:1562px;height:416px;background:linear-gradient(90deg,#ffffff 30%,#f1f1f1 75%,#fafafa)}
.how h2{position:absolute;left:122px;top:82px;font-size:32px;color:#222}
.how p{position:absolute;left:122px;width:434px;font-size:13px;line-height:20px;color:var(--text-soft)}
.how .p1{top:140px}.how .p2{top:196px;text-align:justify}
.btn-orange{position:absolute;left:122px;top:275px;width:145px;height:40px;line-height:40px;background:var(--orange);color:var(--white)}
.globe-art{position:absolute;left:720px;top:60px;width:290px;height:290px;border-radius:50%;background:radial-gradient(circle at 45% 45%,#ffffff 0%,#e4e4e4 55%,#bdbdbd 100%)}

/* get started */
.start{top:1978px;height:368px;background:radial-gradient(ellipse at 40% 40%,#3a444b 0%,#1e2429 60%,#121518 100%);text-align:center;color:var(--white)}
.start h2{font-size:34px;margin-top:85px}
.start p{width:640px;margin:10px auto 0;font-size:14px;line-height:23px;color:#cfd3d6}
.start .btn-red{left:518px;top:236px;width:146px}

/* news */
.news{top:2346px;height:590px}
.news h2{position:absolute;left:120px;top:48px;font-size:30px;color:#222}
.card{position:absolute;top:112px;background:var(--white);border:1px solid var(--line);box-shadow:0 1px 3px rgba(0,0,0,.06)}
.card-feature{left:120px;width:516px;height:422px}
.feature-img{width:100%;height:242px;background:linear-gradient(135deg,#c8c8c8 0%,#e2c271 40%,#b88a2c 70%,#9a9a9a 100%)}
.card-feature h3{font-size:19px;color:#222;margin:22px 0 0 38px}
.date{color:var(--red);font-size:11px}
.card-feature .date{display:block;margin:10px 0 0 38px}
.card-feature p{font-size:11px;line-height:17px;color:var(--text-soft);margin:4px 38px 0}
.read-more{font-size:11px;font-weight:600;color:var(--green);display:block}
.card-feature .read-more{margin:3px 0 0 38px}
.card-list{left:648px;width:430px;height:422px;padding:16px 0 0 16px}
.news-item{display:flex;gap:22px;height:135px}
.thumb{width:146px;height:108px;flex:none}
.t1{background:linear-gradient(135deg,#e4e8ec,#b99545 60%,#6d6b69)}
.t2{background:linear-gradient(135deg,#3a3028,#c19a45 55%,#5f5a52)}
.t3{background:linear-gradient(135deg,#d7e5ef,#3f8fc7 60%,#eef3f6)}
.news-item h4{font-size:15px;color:#222;margin-top:4px}
.news-item .date{display:block;margin-top:8px}
.news-item p{font-size:11px;line-height:17px;color:var(--text-soft);width:220px;margin-top:3px}

/* press */
.press{top:2936px;height:94px;display:flex;align-items:center;justify-content:space-between;padding:0 124px}
.press span{height:36px;background:#9a9a9a;border-radius:4px;opacity:.75}

/* footer */
.site-footer{top:3030px;height:260px;background:linear-gradient(180deg,var(--yellow-light),var(--yellow))}
.footer-col{position:absolute;top:58px}
.footer-col h4{font-size:18px;font-weight:600;color:#222;margin-bottom:12px}
.footer-col li{list-style:none;font-size:13px;line-height:31px;color:#222}
.footer-col p{font-size:11px;line-height:18px;color:#222;width:260px}
.social{display:flex;gap:6px}
.social span{width:32px;height:32px;border-radius:50%;border:2px solid #222}
.footer-bar{top:3290px;height:62px;background:var(--yellow);border-top:1px solid rgba(0,0,0,.05);text-align:center;font-size:11px;line-height:62px;color:#333}
</style>
</head>
<body>

<header class="section site-header">
  <div class="brand"><span class="brand-mark"></span><span class="brand-name">Brook Forge</span></div>
  <nav class="main-nav">
    <a class="active">Home</a><a>About Us</a><a>Our Services</a><a>Why Us</a><a>News</a><a>Blog</a><a>Contact</a>
  </nav>
</header>

<section class="section hero" role="img" aria-label="Wind turbines and solar panels on green hills under a cloudy sky">
  <h1 class="hero-title">CRYPTO CURRENCY MINER</h1>
  <p class="hero-sub">Class aptent taciti sociosqu ad litora torquent per conubia nostra per inceptos hymenaeos Proin nulla</p>
  <a class="btn btn-outline">Learn More</a>
  <div class="slider-dots"><span class="off"></span><span></span><span></span><span></span></div>
</section>

<section class="section intro">
  <div class="network-art" role="img" aria-label="Light grey network of connected nodes with coin symbols forming a dome"></div>
  <h2 class="intro-title">Brook Forge</h2>
  <div class="divider"><i></i><b></b><i></i></div>
  <p class="intro-text">Praesent elementum elit at tellus nec ultricies sit amet porttitor mattis enim In massa libero interdum nec interdum vel blandit sed nulla In ullamcorper est eget tempor cursus neque mi consectetuer mi a ultricies massa est sed nisl Class aptent taciti sociosqu ad li</p>
  <a class="btn btn-red">Learn More</a>
</section>

<section class="section services">
  <h2 class="services-title">Our Services</h2>
  <div class="service-list">
    <div class="service">
      <div class="service-icon"><svg width="56" height="56" viewBox="0 0 56 56" fill="none" stroke="#fff" stroke-width="2"><circle cx="28" cy="22" r="14"/><path d="M8 44h14l10 4 16-8"/></svg></div>
      <h3>Mining is<br>Already Running</h3>
      <p>Class aptent taciti sociosqu ad litora torquent per conubia nostra per inceptos</p>
      <a class="btn btn-outline">Read More</a>
    </div>
    <div class="service">
      <div class="service-icon"><svg width="56" height="56" viewBox="0 0 56 56" fill="none" stroke="#fff" stroke-width="2"><rect x="8" y="8" width="40" height="34"/><path d="M14 34l9-10 7 6 12-14M28 42v8M18 50h20"/></svg></div>
      <h3>Mine Alternative<br>Cryptocurrencies</h3>
      <p>Class aptent taciti sociosqu ad litora torquent per conubia nostra per inceptos</p>
      <a class="btn btn-outline">Read More</a>
    </div>
    <div class="service">
      <div class="service-icon"><svg width="56" height="56" viewBox="0 0 56 56" fill="none" stroke="#fff" stroke-width="2"><rect x="8" y="16" width="40" height="30" rx="3"/><path d="M14 16l18-8 6 8"/><circle cx="28" cy="31" r="7"/></svg></div>
      <h3>Get the First<br>Payout Today</h3>
      <p>Class aptent taciti sociosqu ad litora torquent per conubia nostra per inceptos</p>
      <a class="btn btn-outline">Read More</a>
    </div>
  </div>
</section>

<section class="section how">
  <h2>How it Works</h2>
  <p class="p1">Lommodo a mi Morbi ornare gravida elit Integer congue augue et malesuada iaculis ipsum dui aliquet felis at</p>
  <p class="p2">Aursus magna nisl nec elit Praesent elementum elit at tellus nec ultricies sit amet porttitor mattis enim In massa libero interdum nec interdum vel blandit sed nulla</p>
  <a class="btn btn-orange">Learn More</a>
  <div class="globe-art" role="img" aria-label="Grey wireframe globe of linked nodes with coin symbols and scattered particles"></div>
</section>

<section class="section start" role="img" aria-label="Dark close-up of a laptop screen with a coin graphic">
  <h2>Get Started Now</h2>
  <p>nunc quam venenatis nec euismod sit amet egestas placerat est Pellentesque habitant morbi tristique senectus et netus et malesuada fames ac turpis egestas Cras id elit Integer quis urna Ut ante enim dapibus malesuada fringilla</p>
  <a class="btn btn-red">Learn More</a>
</section>

<section class="section news">
  <h2>News &amp; Blogs</h2>
  <article class="card card-feature">
    <div class="feature-img" role="img" aria-label="Gold and silver crypto coins resting on a keyboard"></div>
    <h3>Pellentesque faucibus Ut accumsan ultricies</h3>
    <span class="date">25 Jan 2018</span>
    <p>netus et malesuada fames ac turpis egestas Cras id elit Integer quis urna Ut ante enimClass aptent taciti sociosqu ad litora torquent per conubia nostra per inceptos hymenaeos Proin nulla arcu nonummy luctus</p>
    <a class="read-more">READ MORE</a>
  </article>
  <div class="card card-list">
    <article class="news-item">
      <div class="thumb t1" role="img" aria-label="Stacked coins beside a rising market chart"></div>
      <div><h4>Nulla sit amet diam</h4><span class="date">25 Jan 2018</span><p>netus et malesuada fames ac turpis egestas Cras id elit Integer quis urna</p><a class="read-more">READ MORE</a></div>
    </article>
    <article class="news-item">
      <div class="thumb t2" role="img" aria-label="Gold coin lying on paper banknotes"></div>
      <div><h4>Etiam est nunc ven</h4><span class="date">25 Jan 2018</span><p>netus et malesuada fames ac turpis egestas Cras id elit Integer quis urna</p><a class="read-more">READ MORE</a></div>
    </article>
    <article class="news-item">
      <div class="thumb t3" role="img" aria-label="Hand holding a card over a blue screen"></div>
      <div><h4>Aliquam erat volutpa</h4><span class="date">25 Jan 2018</span><p>netus et malesuada fames ac turpis egestas Cras id elit Integer quis urna</p><a class="read-more">READ MORE</a></div>
    </article>
  </div>
</section>

<section class="section press" aria-label="Featured in">
  <span style="width:70px"></span><span style="width:110px"></span><span style="width:110px"></span><span style="width:118px"></span><span style="width:92px"></span><span style="width:212px"></span>
</section>

<footer class="section site-footer">
  <div class="footer-col" style="left:116px"><h4>About Us</h4><p>eget tempor cursus neque mi consectetuer mi a ultricies massa est sed nisl Class aptent taciti sociosqu ad litora torquent per conubia nostra per inceptos hymenaeos Proin nulla arcu nonummy</p></div>
  <div class="footer-col" style="left:411px"><h4>Quick Links</h4><ul><li>What We Do</li><li>Blogs</li><li>Services</li><li>Our Blogs</li></ul></div>
  <div class="footer-col" style="left:593px"><h4>Sublinks</h4><ul><li>Class aptent</li><li>Taciti sociosqu</li><li>Pd litora</li><li>Rorquent</li></ul></div>
  <div class="footer-col" style="left:770px"><h4>Resources</h4><ul><li>Articles</li><li>FAQ</li><li>Contact</li></ul></div>
  <div class="footer-col" style="left:934px"><h4>Get in Touch</h4><div class="social"><span></span><span></span><span></span><span></span></div></div>
</footer>
<div class="section footer-bar">© 2018 Company Name &nbsp;All right reserved &nbsp;Term of Use</div>

</body>
</html>
```